Lumbrix - "Where Pest Control is Free for Life..." Please see pitch deck...

Project goal, that this is a reusable template, not a one-off card
Brand and design direction, follow the logo, use the brand palette (with a color swatch table), typography and layout guidance
The John Doe placeholder content as a clean field-by-field table (name, title, company, address, office, cell, fax, email, lumbrix.example)
Print specs, 3.5 × 2 in trim, 0.125 in bleed, 300 DPI, CMYK, crop marks
Deliverables, layered editable PSD (your primary ask) plus vector .AI/.EPS and a press-ready PDF/X-1a, with fonts packaged
What you'll provide (logo, colors, fonts)
Process and sign-off, concept first, then full file package on approval.
Populate every field with this John Doe placeholder data so we can see the layout fully built out. We will replace it per person.
Name John Doe
Title Title / Position
Company Lumbrix
Address 48 Orchard Lane, Suite 210, Marlow Springs, FL 32950
Office (407) 555-0142
Cell (407) 555-0178
Fax (407) 555-0196
Email johndoe@lumbrix.example
Website lumbrix.example

We need the working, editable source files so we can update them ourselves, plus a ready-to-print export:
1. Photoshop (.PSD) — fully layered and editable, with each contact field on its own labeled text layer. This is the primary requested format.
2. Vector source — the press-standard editable format, Adobe Illustrator (.AI) and/or .EPS, since vector is preferred for crisp text and logos at print.
3. Print-ready PDF — press-quality (PDF/X-1a), CMYK, with bleed and crop marks, both sides.
4. Packaged fonts and links — include or list all fonts used, and package any linked assets so the files open correctly on our end.

Why both PSD and vector
The PSD covers our request directly and is easy for us to edit. Vector (.AI/.EPS) is what most commercial printers actually prefer for type and logos because it stays razor-sharp at any size. Providing both keeps us flexible no matter which printer we use. Have fun and keep it modern and cool the designer of the logo did a great job, see what you can do.

```html
<!DOCTYPE html>
<html lang="en">
<head>
<meta charset="utf-8">
<title>Lumbrix Business Card – Front and Back</title>
<link rel="stylesheet" href="https://fonts.googleapis.com/css2?family=Lato:wght@400;700;900&display=swap">
<style>
  :root {
    --stage: #e8e8e8;
    --card-navy: #0b1224;
    --pattern-navy: #0f1a2c;
    --brand-teal: #06b3c7;
    --text-white: #ffffff;
  }
  * { box-sizing: border-box; margin: 0; padding: 0; }
  html, body {
    width: 1200px;
    height: 960px;
    overflow: hidden;
    background: var(--stage);
    font-family: "Lato", Arial, sans-serif;
  }
  .card {
    position: absolute;
    width: 732px;
    height: 418px;
    background: var(--card-navy);
    color: var(--text-white);
    overflow: hidden;
  }
  .card--front { left: 102px; top: 52px; }
  .card--back { left: 350px; top: 499px; }

  .wordmark {
    position: absolute;
    font-weight: 900;
    color: var(--text-white);
    letter-spacing: -1px;
    line-height: 1;
    white-space: nowrap;
  }
  .card--front .wordmark { left: 50px; top: 156px; font-size: 62px; }

  .divider {
    position: absolute;
    left: 380px;
    top: 76px;
    width: 2px;
    height: 254px;
    background: var(--brand-teal);
    border-radius: 2px;
  }

  .identity { position: absolute; left: 449px; top: 76px; }
  .identity__name {
    font-size: 37px;
    font-weight: 900;
    color: var(--brand-teal);
    line-height: 1;
    letter-spacing: -0.3px;
  }
  .identity__company {
    font-size: 20px;
    font-weight: 400;
    margin-top: 2px;
  }

  .contact-list {
    position: absolute;
    left: 449px;
    list-style: none;
  }
  .contact-list--phones { top: 176px; }
  .contact-list--online { top: 278px; }
  .contact-list li {
    display: flex;
    align-items: center;
    height: 24.5px;
    font-size: 20px;
    font-weight: 400;
  }
  .contact-icon {
    width: 18px;
    height: 18px;
    margin-right: 11px;
    flex: none;
    fill: var(--brand-teal);
  }

  .address-band {
    position: absolute;
    left: 0;
    top: 355px;
    width: 100%;
    height: 34px;
    background: var(--brand-teal);
    display: flex;
    align-items: center;
    padding-left: 128px;
    font-size: 20px;
  }
  .address-band .contact-icon { fill: var(--text-white); width: 20px; height: 22px; margin-right: 8px; }

  .back-pattern {
    position: absolute;
    inset: 0;
    background: radial-gradient(circle at 50% 50%, var(--pattern-navy), var(--card-navy));
  }
  .card--back .wordmark {
    left: 50%;
    top: 50%;
    transform: translate(-50%, -45%);
    font-size: 92px;
  }
</style>
</head>
<body>

<section class="card card--front" aria-label="Business card front">
  <div class="wordmark">Lumbrix</div>
  <div class="divider"></div>

  <div class="identity">
    <h1 class="identity__name">JOHN DOE</h1>
    <p class="identity__company">Company Lumbrix</p>
  </div>

  <ul class="contact-list contact-list--phones">
    <li>
      <svg class="contact-icon" viewBox="0 0 24 24" aria-hidden="true"><path d="M6.6 10.8a15 15 0 0 0 6.6 6.6l2.2-2.2c.3-.3.7-.4 1-.2 1.1.4 2.3.6 3.6.6.6 0 1 .4 1 1V20c0 .6-.4 1-1 1A17 17 0 0 1 3 4c0-.6.4-1 1-1h3.5c.6 0 1 .4 1 1 0 1.3.2 2.5.6 3.6.1.3 0 .7-.2 1z"/></svg>
      (407) 555-0142
    </li>
    <li>
      <svg class="contact-icon" viewBox="0 0 24 24" aria-hidden="true"><path d="M7 2h10a2 2 0 0 1 2 2v16a2 2 0 0 1-2 2H7a2 2 0 0 1-2-2V4a2 2 0 0 1 2-2zm0 3v12h10V5z"/></svg>
      (407) 555-0178
    </li>
    <li>
      <svg class="contact-icon" viewBox="0 0 24 24" aria-hidden="true"><path d="M7 2h10v6H7zM3 10h18v7h-3v-3H6v3H3zm4 6h10v6H7z"/></svg>
      (407) 555-0196
    </li>
  </ul>

  <ul class="contact-list contact-list--online">
    <li>
      <svg class="contact-icon" viewBox="0 0 24 24" aria-hidden="true"><path d="M12 2 2 9v12h20V9zm0 3 7 5-7 4-7-4z"/></svg>
      johndoe@lumbrix.example
    </li>
    <li>
      <svg class="contact-icon" viewBox="0 0 24 24" aria-hidden="true"><circle cx="12" cy="12" r="9" fill="none" stroke="currentColor" stroke-width="0"/><path d="M12 2a10 10 0 1 0 0 20 10 10 0 0 0 0-20zm0 2c.9 0 2.1 2.2 2.5 5h-5C9.9 6.2 11.1 4 12 4zm-5.3 7H4.3a8 8 0 0 1 3.5-5.3A15 15 0 0 0 6.7 11zm0 2a15 15 0 0 0 1.1 5.3A8 8 0 0 1 4.3 13zm2.8 0h5c-.4 2.8-1.6 5-2.5 5s-2.1-2.2-2.5-5zm0-2h5v0zm7.8 0a15 15 0 0 0-1.1-5.3 8 8 0 0 1 3.5 5.3zm0 2h2.4a8 8 0 0 1-3.5 5.3 15 15 0 0 0 1.1-5.3z"/></svg>
      lumbrix.example
    </li>
  </ul>

  <div class="address-band">
    <svg class="contact-icon" viewBox="0 0 24 26" aria-hidden="true"><path d="M12 1a8 8 0 0 0-8 8c0 6 8 16 8 16s8-10 8-16a8 8 0 0 0-8-8zm0 11a3 3 0 1 1 0-6 3 3 0 0 1 0 6z"/></svg>
    48 Orchard Lane, Suite 210, Marlow Springs, FL 32950
  </div>
</section>

<section class="card card--back" aria-label="Business card back">
  <div class="back-pattern" role="img" aria-label="Faint repeating brand-symbol pattern across the back of the card"></div>
  <div class="wordmark">Lumbrix</div>
</section>

</body>
</html>
```